Updated brief for New ecommerce site needs a stunning business card that links to web site.

Updated business card brief. Please refer to the new files uploaded today (the last two) which show the background colour/style that we will be using in our web template for on-line trading, the grey marble concrete look.

Please see if you can use the grey marble background in the business card design in a way so it relates to our web template. It also needs to be transferable to banner ad, chatterbox ad etc.
vantor hub is a NEW eCommerce website which is commencing selling via bidnook & swapcrate, used & damaged mobile phones & accessories, evolving into a full eCommerce store.

We like strong clean lines, use of a circle, in essence this will become our logo as well. Colours strong orange/Black/White The orange stronger than in PixelHerd #8164937 & grey marble as per file attached #274615

We love the use of a circle!! As we are evolving & moving forward this is what the circle represents to us……. ongoing change.

Front side with a circle with vantor hub in a modern font in the middle, vantor is in a strong orange and group is in black or white. On the reverse side, use layout as per Snapwell design from plonk.com. for icon details (not the boarder at top/botto).

This design is to meet www.plonk.com luxe cards specifications
Thank you we look forward to last minute inspiration.

Project Deadline Extended Reason: Hi We need to extend our deadline to ensure we don't rush the design. We are close to getting what we want, however due to work commitments here we need a couple more days to work this through to ensure the concept ties in with our other marketing.Thank you for understanding and your patience.vantorhub Added Tuesday, March 3, 2015

Target Market(s)

Suppliers & business networking

Industry/Entity Type

Business

Contact Information for Business Card

Liam Presk
Director
mob +61 4987 6543
Locked Bag WXYZ 5678 QRS
liam@vantorhub.example.au
www.vantorhub.example.au

Requirements
Must have
• Design to meet www.plonk.com luxe business card specifications
• Colours - orange needs to be bold and strong & /black/white
• Circle with vantor hub in the middle
Nice to have
• Grey marble background incorporated into design in someway so it links with our web page.

```html
<!DOCTYPE html>
<html lang="en">
<head>
<meta charset="utf-8">
<title>vantor hub business card</title>
<link rel="stylesheet" href="https://fonts.googleapis.com/css2?family=Fira+Sans:wght@400;600;700&display=swap">
<style>
  :root {
    --orange: #f08c00;
    --charcoal: #2b2b2b;
    --ink: #1e1e1e;
    --paper: #ffffff;
    --backdrop: #e4e4e4;
    --ghost: #ececec;
  }
  * { margin: 0; padding: 0; box-sizing: border-box; }
  html, body { width: 1200px; height: 900px; overflow: hidden; }
  body {
    background: var(--backdrop);
    font-family: "Fira Sans", sans-serif;
    position: relative;
  }
  .card {
    position: absolute;
    top: 180px;
    width: 330px;
    height: 540px;
    box-shadow: 0 6px 18px rgba(0,0,0,0.18);
    overflow: hidden;
  }

  /* Front */
  .card-front { left: 180px; background: var(--charcoal); }
  .logo-circle {
    position: absolute;
    left: 45px; top: 70px;
    width: 240px; height: 240px;
    border-radius: 50%;
    background: var(--paper);
    border: 3px solid var(--orange);
    display: flex;
    align-items: center;
    justify-content: center;
  }
  .logo-name {
    color: var(--orange);
    font-weight: 700;
    font-size: 54px;
    line-height: 0.9;
    text-align: center;
  }
  .web-row {
    position: absolute;
    left: 0; right: 0; top: 410px;
    display: flex;
    align-items: center;
    justify-content: space-between;
  }
  .web-row .dash { width: 46px; height: 3px; background: var(--orange); }
  .web-address {
    color: var(--paper);
    font-size: 15px;
    letter-spacing: 0.2px;
  }

  /* Back */
  .card-back { left: 690px; background: var(--paper); }
  .rule {
    position: absolute;
    left: 40px;
    width: 3px;
    background: var(--orange);
  }
  .rule-top { top: 0; height: 190px; }
  .rule-bottom { top: 470px; height: 70px; }
  .short-dash {
    position: absolute;
    left: 40px;
    width: 24px; height: 3px;
    background: var(--orange);
  }
  .watermark {
    position: absolute;
    right: 42px; top: 70px;
    writing-mode: vertical-rl;
    transform: rotate(180deg);
    color: var(--ghost);
    font-weight: 600;
    font-size: 50px;
    line-height: 0.95;
    text-align: right;
  }
  .contact {
    position: absolute;
    left: 40px; top: 208px;
    color: var(--ink);
  }
  .person-name { font-weight: 700; font-size: 19px; letter-spacing: 0.3px; }
  .person-role { font-size: 16px; margin-top: 2px; }
  .contact-line {
    display: flex;
    align-items: center;
    gap: 10px;
    font-size: 16px;
    position: absolute;
    left: 40px;
    color: var(--ink);
    white-space: nowrap;
  }
  .icon-dot {
    width: 26px; height: 26px;
    border-radius: 50%;
    background: var(--orange);
    display: flex; align-items: center; justify-content: center;
    flex-shrink: 0;
  }
  .contact-email { top: 300px; }
  .contact-phone { top: 340px; }
  .contact-address { top: 410px; font-size: 17px; }
</style>
</head>
<body>
  <section class="card card-front">
    <div class="logo-circle">
      <div class="logo-name">vantor<br>hub</div>
    </div>
    <div class="web-row">
      <span class="dash"></span>
      <span class="web-address">www.vantorhub.example.au</span>
      <span class="dash"></span>
    </div>
  </section>

  <section class="card card-back">
    <span class="rule rule-top"></span>
    <div class="watermark">vantor<br>hub</div>
    <div class="contact">
      <div class="person-name">LIAM PRESK</div>
      <div class="person-role">director</div>
    </div>
    <span class="short-dash" style="top:270px"></span>
    <div class="contact-line contact-email">
      <span class="icon-dot">
        <svg width="16" height="16" viewBox="0 0 16 16" aria-hidden="true">
          <text x="8" y="12.5" text-anchor="middle" font-family="Fira Sans, sans-serif" font-size="14" fill="#fff">@</text>
        </svg>
      </span>
      <span>liam@vantorhub.example.au</span>
    </div>
    <div class="contact-line contact-phone">
      <span class="icon-dot">
        <svg width="14" height="14" viewBox="0 0 24 24" aria-hidden="true">
          <path fill="#fff" d="M6.6 10.8a15.1 15.1 0 0 0 6.6 6.6l2.2-2.2a1 1 0 0 1 1-.25 11.4 11.4 0 0 0 3.6.57 1 1 0 0 1 1 1V20a1 1 0 0 1-1 1A17 17 0 0 1 3 4a1 1 0 0 1 1-1h3.5a1 1 0 0 1 1 1c0 1.25.2 2.45.57 3.570a1 1 0 0 1-.25 1z"/>
        </svg>
      </span>
      <span>+61 4987 6543</span>
    </div>
    <span class="short-dash" style="top:385px"></span>
    <div class="contact-line contact-address">Locked Bag WXYZ 5678 QRS</div>
    <span class="rule rule-bottom"></span>
  </section>
</body>
</html>
```